Corvanta512 Business Card Redesign

I want to create a design for brand new business cards, I need something exceptional for clear plastic business card design. Please do not submit without it being on a clear design. Photos of the various logo versions attached.

```html
<!DOCTYPE html>
<html lang="en">
<head>
<meta charset="utf-8">
<title>Corvanta512 – Business Card</title>
<link rel="stylesheet" href="https://fonts.googleapis.com/css2?family=Inter:wght@400;500;700&display=swap">
<style>
  :root {
    --backdrop: #d9cfc2;
    --card-fill: rgba(246, 241, 233, 0.72);
    --card-edge: rgba(255, 255, 255, 0.85);
    --gold: #b48a3c;
    --navy: #1f2b4d;
    --ink: #2b2620;
  }
  * { box-sizing: border-box; margin: 0; padding: 0; }
  html, body {
    width: 1200px;
    height: 1047px;
    overflow: hidden;
    background: var(--backdrop);
    font-family: "Inter", sans-serif;
  }
  .canvas {
    position: relative;
    width: 1200px;
    height: 1047px;
  }
  .business-card {
    position: absolute;
    left: 125px;
    top: 263px;
    width: 950px;
    height: 520px;
    border-radius: 28px;
    background: var(--card-fill);
    border: 2px solid var(--card-edge);
    box-shadow: 0 10px 30px rgba(80, 60, 40, 0.15);
    display: flex;
    align-items: center;
  }
  .brand-side {
    width: 500px;
    display: flex;
    flex-direction: column;
    align-items: center;
    gap: 26px;
  }
  .brand-mark {
    width: 150px;
    height: 150px;
    border-radius: 50%;
    background: var(--gold);
    opacity: 0.9;
  }
  .brand-name {
    font-weight: 700;
    font-size: 52px;
    color: var(--gold);
    letter-spacing: 1px;
  }
  .divider {
    width: 2px;
    height: 360px;
    background: var(--navy);
  }
  .contact-side {
    padding-left: 36px;
    color: var(--ink);
  }
  .person-name {
    font-weight: 700;
    font-size: 40px;
    color: var(--gold);
    letter-spacing: 0.5px;
    line-height: 1.1;
  }
  .person-role {
    font-size: 25px;
    margin-top: 10px;
  }
  .coverage {
    margin-top: 24px;
    font-size: 23px;
    line-height: 1.55;
  }
  .contact-list {
    list-style: none;
    margin-top: 22px;
    font-size: 23px;
  }
  .contact-list li {
    display: flex;
    align-items: center;
    gap: 12px;
    line-height: 1.55;
  }
  .contact-list svg {
    width: 20px;
    height: 20px;
    fill: var(--navy);
    flex: none;
  }
</style>
</head>
<body>
<main class="canvas">
  <section class="business-card">
    <div class="brand-side">
      <div class="brand-mark"></div>
      <div class="brand-name">Corvanta512</div>
    </div>
    <div class="divider"></div>
    <div class="contact-side">
      <h1 class="person-name">MARCUS DELANE</h1>
      <p class="person-role">Marketing Manager</p>
      <p class="coverage">Serving clients nationwide<br>All 50 states covered</p>
      <ul class="contact-list">
        <li>
          <svg viewBox="0 0 24 24" aria-hidden="true"><path d="M6.6 10.8a15.1 15.1 0 0 0 6.6 6.6l2.2-2.2c.3-.3.7-.4 1-.2 1.1.4 2.3.6 3.6.6.6 0 1 .4 1 1V20c0 .6-.4 1-1 1A17 17 0 0 1 3 4c0-.6.4-1 1-1h3.5c.6 0 1 .4 1 1 0 1.3.2 2.5.6 3.6.1.3 0 .7-.2 1z"/></svg>
          <span>(833) CRVN-512</span>
        </li>
        <li>
          <svg viewBox="0 0 24 24" aria-hidden="true"><path d="M2 5h20v14H2z M2 5l10 8 10-8" fill="none" stroke="#1f2b4d" stroke-width="2"/></svg>
          <span>info@corvanta-512.com</span>
        </li>
        <li>
          <svg viewBox="0 0 24 24" aria-hidden="true"><circle cx="12" cy="12" r="9" fill="none" stroke="#1f2b4d" stroke-width="2"/><path d="M3 12h18M12 3c3 3 3 15 0 18M12 3c-3 3-3 15 0 18" fill="none" stroke="#1f2b4d" stroke-width="1.6"/></svg>
          <span>corvanta-512.com</span>
        </li>
      </ul>
    </div>
  </section>
</main>
</body>
</html>
```